Verandel Windows & Doors

We are an aluminum windows & doors manufacturer. Need a professional & vision appealing web design. It should reflects our professional business character, but with very user-friendly interface( catch eyes, use simple icon or symbol to make it easy to read...) Don't copy : ) but can use some competitor's web (https://www.polkrenwindows.example) (www.brivatglazing.example.au) to have a glance on our target and web content as reference

Target Market(s)

Homeowner and Professional (Builder / Developer/ Architect & window installer)

Industry/Entity Type

Manufacturer

Font styles to use
Serif
Sans Serif

Requirements
Must have
• Have 3 serials products. Residential (value for money) Commercial (Professional and quality) Architectural (Bold & funky)
• Color match or harmony with the selected logo design
Nice to have
• Project gallery display, have online free quote to upload files, can insert video or cartoon
Should not have
• no limitation on your imagination ; )

```html
<!DOCTYPE html>
<html lang="en">
<head>
<meta charset="utf-8">
<title>Verandel Windows &amp; Doors</title>
<link href="https://fonts.googleapis.com/css2?family=Open+Sans:wght@400;600;700&family=PT+Serif:wght@400;700&display=swap" rel="stylesheet">
<style>
  :root{
    --green:#8bc34a;
    --green-dark:#6fa33a;
    --slate:#3e4a6c;
    --bg:#eceeea;
    --band:#d6dad1;
    --text:#5b5f58;
    --heading:#6d7a63;
    --white:#ffffff;
    --footer:#4a4f48;
    --photo-sky:#6d8fb0;
    --photo-house:#8a7e6e;
  }
  *{box-sizing:border-box;margin:0;padding:0}
  html,body{width:849px;height:1200px;overflow:hidden}
  body{font-family:"Open Sans",Arial,sans-serif;color:var(--text);background:var(--bg);font-size:10px;line-height:1.45}
  .page{width:849px;height:1200px;display:flex;flex-direction:column}

  .site-header{height:160px;display:flex;flex:none}
  .brand{width:240px;background:#f4f5f1;display:flex;flex-direction:column;justify-content:center;padding-left:28px}
  .brand-row{display:flex;align-items:center;gap:8px}
  .brand-mark{width:16px;height:16px;background:var(--green)}
  .brand-name{font-size:19px;font-weight:700;color:var(--heading);letter-spacing:1px}
  .brand-tagline{margin-top:6px;font-size:13px;color:var(--green-dark)}
  .header-photo{flex:1;background:linear-gradient(180deg,var(--photo-sky) 0%,#a7b6c4 45%,var(--photo-house) 100%)}

  .main-nav{height:30px;flex:none;background:var(--band);display:flex;align-items:center;padding-left:14px;gap:4px}
  .nav-link{font-size:9px;color:#4d5249;padding:5px 12px}
  .nav-link.is-active{background:var(--green);color:var(--white)}

  .hero{height:264px;flex:none;display:flex}
  .hero-photo{width:470px;background:linear-gradient(160deg,#c9c5b8 0%,#9aa58c 40%,#6f7a62 100%)}
  .hero-panel{flex:1;background:var(--slate);color:var(--white);padding:30px 26px}
  .hero-title{font-size:14px;font-weight:700;line-height:1.5}
  .hero-title strong{font-family:"PT Serif",Georgia,serif;font-size:21px}
  .hero-text{margin-top:8px;font-size:9.5px;color:#d8dde8}
  .btn{display:inline-block;background:var(--green);color:var(--white);font-size:9px;padding:6px 16px;margin-top:20px}

  .columns{height:304px;flex:none;display:flex;gap:26px;padding:20px 24px}
  .col{flex:1}
  .col-title{font-size:12px;color:var(--heading);padding-bottom:6px;border-bottom:1px solid #cfd3c9;margin-bottom:12px}
  .news-item{display:flex;gap:10px;margin-bottom:12px}
  .news-thumb{width:58px;height:44px;flex:none}
  .news-date{color:var(--green-dark);font-size:9px}
  .news-text{font-size:9px}
  .window-body{display:flex;gap:10px}
  .window-photo{width:110px;height:130px;flex:none;background:linear-gradient(180deg,#b8b2a4,#76705f)}
  .window-text p{font-size:9px;margin-bottom:8px}
  .window-note{font-size:9px;margin-top:8px}
  .service-list{list-style:none}
  .service-list li{font-size:9px;padding:4px 0;border-bottom:1px dotted #cfd3c9;display:flex;align-items:center;gap:6px}

  .social-row{height:152px;flex:none;display:flex;gap:26px;padding:6px 24px 0}
  .follow{width:240px}
  .follow-title{font-size:12px;color:var(--heading);margin-bottom:10px}
  .social-icons{display:flex;gap:8px}
  .social-icon{width:32px;height:32px;border-radius:4px;background:#7d8a96}
  .testimonial{flex:1;height:116px;position:relative;background:#dfe2db;padding:14px 18px}
  .testimonial-title{font-family:"PT Serif",Georgia,serif;font-size:14px;color:var(--heading);margin-bottom:6px}
  .testimonial-text{font-size:9px}
  .bubble-tail{position:absolute;right:40px;bottom:-14px}

  .video-gallery{height:210px;flex:none;padding-top:4px;text-align:center}
  .video-heading{font-family:"PT Serif",Georgia,serif;font-size:15px;font-weight:700;color:#4d5249;line-height:1.3}
  .video-heading span{font-weight:400}
  .video-strip{margin:10px 24px 0;background:#2f312e;display:flex;gap:8px;padding:8px}
  .video-thumb{flex:1;height:128px;position:relative}
  .play{position:absolute;left:50%;top:50%;transform:translate(-50%,-50%)}

  .category-band{height:40px;flex:none;background:#c9d8b6;display:flex;align-items:center;justify-content:space-around;padding:0 24px}
  .category{font-size:9px;font-weight:700;color:var(--green-dark);letter-spacing:.5px}
  .site-footer{flex:1;background:var(--footer);color:#c8ccc4;font-size:8px;display:flex;align-items:center;padding-left:24px}
</style>
</head>
<body>
<div class="page">

  <header class="site-header">
    <div class="brand">
      <div class="brand-row"><span class="brand-mark"></span><span class="brand-name">VERANDEL</span></div>
      <div class="brand-tagline">solutions that you need!</div>
    </div>
    <div class="header-photo" role="img" aria-label="Photo of a modern two-storey house at dusk"></div>
  </header>

  <nav class="main-nav">
    <span class="nav-link is-active">Home</span>
    <span class="nav-link">Windows</span>
    <span class="nav-link">Doors</span>
    <span class="nav-link">Gates</span>
    <span class="nav-link">Contacts</span>
  </nav>

  <section class="hero">
    <div class="hero-photo" role="img" aria-label="Photo of a patio with large glass sliding doors and garden furniture"></div>
    <div class="hero-panel">
      <h1 class="hero-title">Let's Create<br>Your Growth Strategy <strong>Together</strong></h1>
      <p class="hero-text">We design and build aluminium windows and doors for homes, builders and architects. Strong frames, slim lines and a finish made to last for years in every season.</p>
      <span class="btn">Learn more</span>
    </div>
  </section>

  <section class="columns">
    <div class="col">
      <h2 class="col-title">What's New</h2>
      <div class="news-item">
        <div class="news-thumb" role="img" aria-label="Thumbnail of a living room with windows" style="background:linear-gradient(135deg,#b4ad9c,#7e7766)"></div>
        <div><div class="news-date">Jan 08, 12</div><div class="news-text">New slimline sliding door range is now ready for quotes and site visits.</div></div>
      </div>
      <div class="news-item">
        <div class="news-thumb" role="img" aria-label="Thumbnail of a glazed office front" style="background:linear-gradient(135deg,#9fb0c0,#5f6f80)"></div>
        <div><div class="news-date">Dec 20, 11</div><div class="news-text">Our commercial series passed new energy rating tests this month.</div></div>
      </div>
      <div class="news-item">
        <div class="news-thumb" role="img" aria-label="Thumbnail of a modern home exterior" style="background:linear-gradient(135deg,#c3b89f,#8e8168)"></div>
        <div><div class="news-date">Dec 02, 11</div><div class="news-text">See our latest architectural project with bold framed glass walls.</div></div>
      </div>
      <span class="btn" style="margin-top:4px">More news</span>
    </div>

    <div class="col">
      <h2 class="col-title">Window</h2>
      <div class="window-body">
        <div class="window-photo" role="img" aria-label="Photo of an open aluminium framed window"></div>
        <div class="window-text">
          <p>Residential windows give great value for money with smooth tracks and easy care frames.</p>
          <p>Commercial windows offer tough quality for busy sites and long term use.</p>
        </div>
      </div>
      <p class="window-note">Architectural windows are bold and funky, made to order in any size, shape or colour you need.</p>
    </div>

    <div class="col">
      <h2 class="col-title">Services</h2>
      <ul class="service-list">
        <li><svg width="6" height="8"><path d="M0 0L6 4L0 8z" fill="#8bc34a"/></svg>Residential Windows</li>
        <li><svg width="6" height="8"><path d="M0 0L6 4L0 8z" fill="#8bc34a"/></svg>Commercial Glazing</li>
        <li><svg width="6" height="8"><path d="M0 0L6 4L0 8z" fill="#8bc34a"/></svg>Architectural Systems</li>
        <li><svg width="6" height="8"><path d="M0 0L6 4L0 8z" fill="#8bc34a"/></svg>Sliding Doors</li>
        <li><svg width="6" height="8"><path d="M0 0L6 4L0 8z" fill="#8bc34a"/></svg>Bi-fold Doors</li>
        <li><svg width="6" height="8"><path d="M0 0L6 4L0 8z" fill="#8bc34a"/></svg>Security Screens</li>
        <li><svg width="6" height="8"><path d="M0 0L6 4L0 8z" fill="#8bc34a"/></svg>Custom Colours</li>
        <li><svg width="6" height="8"><path d="M0 0L6 4L0 8z" fill="#8bc34a"/></svg>Free Online Quote</li>
      </ul>
      <span class="btn" style="margin-top:14px">Get a quote</span>
    </div>
  </section>

  <section class="social-row">
    <div class="follow">
      <h2 class="follow-title">Follow Us</h2>
      <div class="social-icons">
        <span class="social-icon"></span><span class="social-icon"></span><span class="social-icon"></span><span class="social-icon"></span>
      </div>
    </div>
    <div class="testimonial">
      <h2 class="testimonial-title">Testimonials</h2>
      <p class="testimonial-text">"The team made our new home bright and quiet. The doors slide with one finger and the frames still look new after two winters. Fitting was quick and the site was left clean. We will use them again on our next build and tell our friends too."</p>
      <svg class="bubble-tail" width="24" height="14"><path d="M0 0H24L18 14z" fill="#dfe2db"/></svg>
    </div>
  </section>

  <section class="video-gallery">
    <h2 class="video-heading">Installing Windows &amp; Doors<br><span>(Video Gallery)</span></h2>
    <div class="video-strip">
      <div class="video-thumb" role="img" aria-label="Video still of a shop front with glass doors" style="background:linear-gradient(135deg,#9aa8b4,#4f5a63)">
        <svg class="play" width="26" height="26"><circle cx="13" cy="13" r="13" fill="rgba(255,255,255,.7)"/><path d="M10 7L19 13L10 19z" fill="#3e4a6c"/></svg>
      </div>
      <div class="video-thumb" role="img" aria-label="Video still of a kitchen with orange furniture and wide windows" style="background:linear-gradient(135deg,#d89a5a,#7a5a3c)">
        <svg class="play" width="26" height="26"><circle cx="13" cy="13" r="13" fill="rgba(255,255,255,.7)"/><path d="M10 7L19 13L10 19z" fill="#3e4a6c"/></svg>
      </div>
      <div class="video-thumb" role="img" aria-label="Video still of a frosted glass partition" style="background:linear-gradient(135deg,#d7dadb,#8d9294)">
        <svg class="play" width="26" height="26"><circle cx="13" cy="13" r="13" fill="rgba(255,255,255,.7)"/><path d="M10 7L19 13L10 19z" fill="#3e4a6c"/></svg>
      </div>
    </div>
  </section>

  <nav class="category-band">
    <span class="category">WINDOWS</span>
    <span class="category">DOORS</span>
    <span class="category">ROOF</span>
    <span class="category">OTHERS</span>
  </nav>

  <footer class="site-footer">Copyright © 2012 All Rights Reserved</footer>
</div>
</body>
</html>
```